Brambleton Resource Holdings, LP Letter Head

We need an official company letter head design that is clean and mimics our company logo style. It will include our logo, address, phone, and website. We are an OIl and Gas mineral purchasing company, so hints of oil rigs or related design would be desirable.

Industry/Entity Type

Oil And Gas

Colors
ec1f27
f04a50
f59195
fbd4d5

Requirements
Must have
• Logo
• 7392 Whitcombe R. Ashdale Parkway, Suite 618
• Dallas TX, 75391
• 214-673-1958
• www.bramblestoneres.example
Nice to have
• Oil Rigs or OIl and gas related design

```html
<!DOCTYPE html>
<html lang="en">
<head>
<meta charset="utf-8">
<title>Brambleton Resource Holdings, LP – Letterhead</title>
<link href="https://fonts.googleapis.com/css2?family=Cinzel:wght@400;600&display=swap" rel="stylesheet">
<style>
  :root {
    --brand-red: #ec1f27;
    --brand-red-soft: #f04a50;
    --band-dark: #3a3a3c;
    --paper: #ebebec;
    --backdrop: #d9d9da;
    --skyline: #dcdcdd;
    --ink: #2a2a2a;
  }
  * { margin: 0; padding: 0; box-sizing: border-box; }
  html, body { width: 1200px; height: 800px; overflow: hidden; }
  body {
    background: var(--backdrop);
    font-family: "Cinzel", "Times New Roman", serif;
    color: var(--ink);
  }
  .letterhead {
    position: absolute;
    left: 330px;
    top: 18px;
    width: 540px;
    height: 764px;
    background: var(--paper);
    overflow: hidden;
    box-shadow: 0 6px 18px rgba(0,0,0,0.18);
  }
  .side-band {
    position: absolute;
    top: 0;
    bottom: 0;
    width: 14px;
    background: var(--band-dark);
  }
  .side-band--left { left: 0; }
  .side-band--right { right: 0; }
  .corner-accent {
    position: absolute;
    width: 96px;
    height: 60px;
  }
  .corner-accent--top { left: 0; top: 0; }
  .corner-accent--bottom { right: 0; bottom: 0; transform: rotate(180deg); }

  .brand {
    position: absolute;
    top: 44px;
    left: 190px;
    width: 260px;
    display: flex;
    align-items: center;
    gap: 10px;
    color: var(--brand-red);
    font-weight: 600;
  }
  .brand__square {
    flex: none;
    width: 34px;
    height: 34px;
    background: var(--brand-red);
  }
  .brand__name {
    font-size: 17px;
    line-height: 1.1;
    letter-spacing: 0.04em;
  }

  .oilfield-scene {
    position: absolute;
    left: 14px;
    bottom: 0;
    width: 330px;
    height: 360px;
    background: linear-gradient(to top, var(--skyline) 0%, var(--skyline) 45%, rgba(220,220,221,0.4) 80%, rgba(220,220,221,0) 100%);
  }

  .contact {
    position: absolute;
    display: flex;
    align-items: center;
    gap: 10px;
    font-size: 9px;
    letter-spacing: 0.04em;
    line-height: 1.45;
  }
  .contact--address { left: 30px; bottom: 30px; }
  .contact--web { right: 36px; bottom: 30px; text-align: right; }
  .contact__icon {
    flex: none;
    width: 20px;
    height: 20px;
  }
</style>
</head>
<body>
  <main class="letterhead">
    <div class="side-band side-band--left"></div>
    <div class="side-band side-band--right"></div>

    <svg class="corner-accent corner-accent--top" viewBox="0 0 96 60" aria-hidden="true">
      <path d="M0 0 H96 C60 4 30 22 14 60 H0 Z" fill="var(--brand-red)"/>
    </svg>
    <svg class="corner-accent corner-accent--bottom" viewBox="0 0 96 60" aria-hidden="true">
      <path d="M0 0 H96 C60 4 30 22 14 60 H0 Z" fill="var(--brand-red)"/>
    </svg>

    <header class="brand">
      <span class="brand__square"></span>
      <span class="brand__name">Brambleton Resource Holdings</span>
    </header>

    <div class="oilfield-scene" role="img" aria-label="Faint grey silhouette of an offshore oil platform, drilling derricks and pump jacks"></div>

    <footer>
      <div class="contact contact--address">
        <span>7392 Whitcombe R. Ashdale Parkway<br>Suite 618, Dallas TX, 75391</span>
        <svg class="contact__icon" viewBox="0 0 20 20" aria-hidden="true">
          <circle cx="10" cy="10" r="9" fill="none" stroke="var(--ink)" stroke-width="1.2"/>
          <path d="M10 5 L15 9.5 H13.5 V14 H6.5 V9.5 H5 Z" fill="var(--brand-red)"/>
        </svg>
      </div>
      <div class="contact contact--web">
        <svg class="contact__icon" viewBox="0 0 20 20" aria-hidden="true">
          <circle cx="10" cy="10" r="9" fill="none" stroke="var(--ink)" stroke-width="1.2"/>
          <circle cx="10" cy="10" r="5" fill="var(--brand-red)"/>
        </svg>
        <span>214-673-1958<br>www.bramblestoneres.example</span>
      </div>
    </footer>
  </main>
</body>
</html>
```